Brochure Design - Non-Profit Fundraising Stream

We are a non-profit organization that is developing a fundraising project through the donation of life insurance policies. We have three brochures in each English and French that we developed for a sister organization that we want to reintegrate with our Foundation, keeping the same copy text just changing the logos, colors and make it overall more visually appealing. The foundation is called the 'Varnek-Holt Syndrome Foundation Canada'.
The original files in .docx format are attached as is the full logo and two symbol files. The deliverables would be six documents in total (InDesign or .docx), each brochure in English and French. The color hex codes are:
red: #7b2850
dark blue: #2c79a7
pale blue: #78b2e2

```html
<!DOCTYPE html>
<html lang="en">
<head>
<meta charset="utf-8">
<title>Varnek-Holt Syndrome Foundation Canada – Donor Brochures</title>
<link rel="stylesheet" href="https://fonts.googleapis.com/css2?family=Ubuntu:wght@300;400;500;700&display=swap">
<style>
:root{
  --blue:#2c79a7;
  --pale:#78b2e2;
  --red:#7b2850;
  --ink:#2b2b2b;
  --board:#d8dadb;
  --white:#ffffff;
  --rule:#9cc3e3;
}
*{box-sizing:border-box;margin:0;padding:0}
html,body{width:667px;height:1200px;overflow:hidden}
body{background:linear-gradient(180deg,#dfe1e2,#d2d4d5);font-family:"Ubuntu",sans-serif;color:var(--ink);position:relative}
.page{position:absolute;width:234px;height:331px;background:var(--white);overflow:hidden;display:flex;flex-direction:column;box-shadow:0 1px 3px rgba(0,0,0,.18)}
.col-left{left:89px}.col-right{left:344px}
.row-1{top:70px}.row-2{top:435px}.row-3{top:801px}

.masthead{height:56px;position:relative;flex:none}
.masthead-pattern{position:absolute;right:0;top:0;width:160px;height:56px;background:radial-gradient(ellipse at 100% 0%,#dbe9f6 0%,rgba(219,233,246,.4) 45%,rgba(255,255,255,0) 75%)}
.brand{position:absolute;left:17px;top:19px;color:var(--blue);font-weight:400;display:flex;align-items:center;gap:4px}
.brand-name{font-size:13px;line-height:1}
.brand-sub{display:block;font-size:4.4px;line-height:1.3}
.brand-mark{width:7px;height:7px;border-radius:50%;background:var(--red);flex:none}
.doc-title{position:absolute;right:20px;top:33px;text-align:right;color:var(--blue);font-weight:300;font-size:7px;line-height:8.5px}
.doc-title.three{top:24px}

.intro{background:var(--blue);color:var(--white);font-size:4.1px;line-height:5.6px;padding:4px 21px 5px;flex:none}
.intro p+p{margin-top:1.5px}
.intro a{color:var(--white);text-decoration:underline}

.section-title{text-align:center;color:var(--blue);font-weight:700;font-size:4.6px;margin:6px 0 4px;letter-spacing:.2px}
.steps{list-style:none;padding:0 31px 0 32px;font-size:4px;line-height:5.1px}
.steps>li{border-bottom:.6px dotted var(--rule);padding:2.4px 0 2.4px 3px}
.steps>li:first-child{padding-top:0}
.steps>li:last-child{border-bottom:none}
.steps .link{color:var(--blue)}
.sub{padding-left:6px}
.sub2{padding-left:12px}

.footer{margin-top:auto;height:11px;background:var(--blue);color:var(--white);font-size:4.2px;line-height:11px;text-align:center;flex:none}

.faq-head{display:grid;grid-template-columns:89px 1fr;background:var(--blue);color:var(--white);font-size:4px;font-weight:500;height:8px;line-height:8px;padding:0 10px;flex:none}
.faq{padding:0 7px 0 10px;font-size:3.9px;line-height:4.9px}
.faq-row{display:grid;grid-template-columns:89px 1fr;border-bottom:.6px dotted var(--rule);padding:1.1px 0}
.faq-row:last-child{border-bottom:none}
.faq-row .q{padding-right:4px}
.faq-row .a{text-align:justify}
.faq ul{list-style:none;padding-left:3px}
.faq li::before{content:"• "}
.faq li.minor{padding-left:3px}
.faq li.minor::before{content:"◦ "}
.faq b{font-weight:700}

.band{background:var(--blue);color:var(--white);text-align:center;font-size:5px;height:11px;line-height:11px;flex:none}
.advantages{padding:6px 14px 0;font-size:3.9px;line-height:5.1px}
.advantages h3{font-size:4.8px;font-weight:400;margin-bottom:1px}
.advantages ol{padding-left:9px}
.split{display:flex;gap:6px;margin-top:4px;align-items:flex-start}
.split p{flex:1;text-align:justify}
.suitable{width:82px;flex:none;background:var(--blue);color:var(--white);padding:3px 3px 3px;font-size:3.7px;line-height:4.6px}
.suitable h4{text-align:center;font-weight:500;font-size:4.8px;margin-bottom:2px}
.suitable li{list-style:none;border-bottom:.5px solid rgba(255,255,255,.45);padding:.6px 0}
.suitable li:last-child{border-bottom:none}
.suitable li::before{content:"• "}
.benefits{padding:4px 30px 4px 17px;font-size:3.9px;line-height:5px;list-style:none}
.benefits li{padding-left:4px;text-indent:-4px}
.benefits li::before{content:"• "}
.flow{display:flex;align-items:center;padding:7px 14px 7px;gap:0}
.flow-step{width:33.5px;height:34px;background:var(--blue);color:var(--white);font-size:3.6px;line-height:4.4px;display:flex;align-items:center;justify-content:center;text-align:center;padding:1px}
.flow-arrow{width:9.5px;display:flex;justify-content:center}
.flow-arrow svg{width:3px;height:4px;display:block}
.page.charity .footer{margin-top:0}
.disclosures{padding:3px 14px 0;font-size:2.5px;line-height:3.2px;color:#444}
.disclosures strong{font-weight:500;display:block}
</style>
</head>
<body>

<!-- English process -->
<section class="page col-left row-1">
  <header class="masthead">
    <div class="masthead-pattern" role="img" aria-label="Soft dotted pattern in pale blue"></div>
    <div class="brand"><div><span class="brand-name">Varnek-Holt</span><span class="brand-sub">Syndrome Foundation Canada</span></div><span class="brand-mark"></span></div>
    <div class="doc-title">Process<br>For Donors</div>
  </header>
  <div class="intro">
    <p><b>Varnek-Holt Syndrome Foundation of Canada (VHSFC)</b> has partnered with ALDERON Charity Services (ACS) to assist <b>VHSF Canada</b> (<a>www.varnekholtcanada.org</a>) to develop a Planned Giving Plus Program to finance medical research and support.</p>
    <p>ALDERON Charity Services (ACS) has developed the following streamlined process to evaluate potential life insurance donations.</p>
  </div>
  <h2 class="section-title">PROCESS</h2>
  <ol class="steps">
    <li>1) Submit case with the following info to <span class="link">donation@varnekholtcanada.org</span>
      <div class="sub">a. Carrier name<br>b. Policy type (term - permanent - universal)<br>c. Policy contract number<br>d. Face value<br>e. Policy issue date<br>f. Policy expiry date<br>g. Premiums and frequency<br>h. Policy trigger (if multiple insureds: first/last to die)<br>i. Age and DOB<br>j. Any known medical issues<br>k. Insured contact information</div>
      <div class="sub2">i. Full name<br>ii. Phone number<br>iii. Email address</div></li>
    <li>2) ACS will review case and indicate interest to advisor</li>
    <li>3) If potential donation meets criteria, ACS will setup medical underwriting call with the insured</li>
    <li>4) Medical underwriting phone interview (Costs assumed by VHSFC)</li>
    <li>5) Within 2 weeks of the call, VHSFC will indicate interest</li>
    <li>6) VHSFC will provide an approximate value of donation receipt</li>
    <li>7) Client confirms intention to donate</li>
    <li>8) VHSFC contracts the actuary to generate the value for the donation receipt (Costs assumed by VHSFC)</li>
    <li>9) Transfer of ownership and advisor completes paperwork accordingly</li>
    <li>10) Insurance company confirms transfer of ownership to Foundation</li>
    <li>11) VHSFC issues tax receipt and thank you letter to donor</li>
    <li>12) Once transfer is confirmed by Carrier, VHSFC converts policy to permanent (if term)</li>
  </ol>
  <footer class="footer">Call Us: 1 (800) 555-0142 | donation@varnekholtcanada.org</footer>
</section>

<!-- French process -->
<section class="page col-right row-1" lang="fr">
  <header class="masthead">
    <div class="masthead-pattern" role="img" aria-label="Motif de points bleu pâle"></div>
    <div class="brand"><div><span class="brand-name">Varnek-Holt</span><span class="brand-sub">Syndrome Foundation Canada</span></div><span class="brand-mark"></span></div>
    <div class="doc-title">Processus<br>Pour Donateurs(trices)</div>
  </header>
  <div class="intro">
    <p>La Fondation du syndrome Varnek-Holt Canada (la Fondation) s’est associée à Services caritatifs ALDERON (SCA), qui aidera la Fondation (<a>www.varnekholtcanada.org</a>) à mettre en place un Programme bonifié de dons planifiés visant à financer la recherche médicale.</p>
    <p>Services caritatifs ALDERON a mis au point le processus simplifié suivant pour lui permettre d’évaluer les dons de polices d’assurance vie.</p>
  </div>
  <h2 class="section-title">PROCESSUS</h2>
  <ol class="steps">
    <li>1) Soumettre le dossier avec l’information qui suit à l’adresse <span class="link">donation@varnekholtcanada.org</span>
      <div class="sub">a. Nom de l’assureur<br>b. Type de police (temporaire - permanente - universelle)<br>c. Numéro du contrat d’assurance<br>d. Valeur nominale<br>e. Date d’émission de la police<br>f. Date d’échéance de la police<br>g. Primes et fréquence<br>h. Déclenchement de la police (si plusieurs assurés : premier/dernier décès)<br>i. Âge et date de naissance<br>j. Tout problème médical connu<br>k. Coordonnées de la personne assurée</div>
      <div class="sub2">i. Nom complet<br>ii. Numéro de téléphone<br>iii. Adresse de courriel</div></li>
    <li>2) SCA examine le dossier et communique son intérêt au conseiller</li>
    <li>3) Si le dossier répond aux critères, SCA organise un appel de souscription médicale avec la</li>
    <li>4) Entrevue téléphonique de souscription médicale (coûts assumés par la Fondation)</li>
    <li>5) Dans les deux semaines de l’appel, la Fondation communique son intérêt</li>
    <li>6) La Fondation donne une estimation de la valeur du reçu de don de bienfaisance</li>
    <li>7) Le client confirme son intention de faire le don</li>
    <li>8) La Fondation charge l’actuaire de générer la valeur du reçu (coûts assumés par la</li>
    <li>9) Transfert de la propriété; le conseiller remplit les documents nécessaires</li>
    <li>10) La compagnie d’assurance confirme le transfert de propriété à la Fondation</li>
    <li>11) La Fondation fait parvenir au donneur un reçu aux fins de l’impôt et une lettre de</li>
    <li>12) Une fois le transfert confirmé par l’assureur, la Fondation convertit la police (si elle est temporaire) en police permanente</li>
  </ol>
  <footer class="footer">Contactez-nous: 1 (800) 555-0142 | donation@varnekholtcanada.org</footer>
</section>

<!-- English FAQ -->
<section class="page col-left row-2">
  <header class="masthead">
    <div class="masthead-pattern" role="img" aria-label="Soft dotted pattern in pale blue"></div>
    <div class="brand"><div><span class="brand-name">Varnek-Holt</span><span class="brand-sub">Syndrome Foundation Canada</span></div><span class="brand-mark"></span></div>
    <div class="doc-title">FAQ<br>For Donors</div>
  </header>
  <div class="faq-head"><span>QUESTIONS</span><span>ANSWERS</span></div>
  <div class="faq">
    <div class="faq-row"><span class="q">What types of policies are eligible?</span><span class="a">Term/permanent (whole life and universal)</span></div>
    <div class="faq-row"><span class="q">Who pays for medical underwriting?</span><span class="a">The Foundation</span></div>
    <div class="faq-row"><span class="q">Who pays for actuarial underwriting?</span><span class="a">The Foundation</span></div>
    <div class="faq-row"><span class="q">What size policies do you accept?</span><span class="a">Between $50k and $10m</span></div>
    <div class="faq-row"><span class="q">What are your selection criteria?</span><span class="a">We are working with a life expectancy (LE) calculation of up to 5 years. However, depending upon the circumstances we could go beyond 5 years. Rule of thumb: insured is 70 years old and over, with a medical condition or 80 years old and over, without medical condition.<br>&nbsp;</span></div>
    <div class="faq-row"><span class="q">Who pays the premiums after the policy has been donated?</span><span class="a">The Foundation</span></div>
    <div class="faq-row"><span class="q">Who is the beneficiary of the policy after it has been donated?</span><span class="a">The Foundation</span></div>
    <div class="faq-row"><span class="q">Who is the owner after the policy has been donated?</span><span class="a">The Foundation</span></div>
    <div class="faq-row"><span class="q">Who does all of the due diligence and underwriting?</span><span class="a">The foundation has partnered with ALDERON Charity Services who looks after these aspects.</span></div>
    <div class="faq-row"><span class="q">How does the process work?</span><span class="a">You call/email us and give us the following information:
      <ul><li>Face value of the policy</li><li>Annual premium (current and renewal)</li><li>Type of policy</li><li class="minor">If term, is it convertible without medical underwriting?</li><li>Policy expiration</li><li>Medical condition(s) of the insured</li><li>Age of the insured</li></ul></span></div>
    <div class="faq-row"><span class="q">How long does the policy have to have been in force for?</span><span class="a">The policy must be in force for over 2 years.</span></div>
    <div class="faq-row"><span class="q">How long does the process take?</span><span class="a">Triage: less than a week<br>Medical underwriting: 1-2 weeks<br>Actuarial underwriting: 1 week<br>Donation paperwork: 1 day<br><b>Total time: 3-4 weeks</b></span></div>
    <div class="faq-row"><span class="q">What is the typical value of the tax receipt that the donor will receive?</span><span class="a">It varies on the life expectancy calculation, which depends on age and medical situation.</span></div>
    <div class="faq-row"><span class="q">What if one of my relatives wanted to benefit from the policy?</span><span class="a">Before a policy donation is approved, we must ensure that no relative is interested in taking over the policy.</span></div>
    <div class="faq-row"><span class="q">Is it legal?</span><span class="a">Yes; the entire process is legal, ethical, and approved by the government.</span></div>
    <div class="faq-row"><span class="q">But what’s in it for me?</span><span class="a">You had planned to cancel your policy in order to save paying the premiums. The Foundation pays the premiums (you save $$) and you get a tax receipt (good for 5 years) which puts money back into your pocket.</span></div>
  </div>
  <footer class="footer">Call Us: 1 (800) 555-0142 | donation@varnekholtcanada.org</footer>
</section>

<!-- French FAQ -->
<section class="page col-right row-2" lang="fr">
  <header class="masthead">
    <div class="masthead-pattern" role="img" aria-label="Motif de points bleu pâle"></div>
    <div class="brand"><div><span class="brand-name">Varnek-Holt</span><span class="brand-sub">Syndrome Foundation Canada</span></div><span class="brand-mark"></span></div>
    <div class="doc-title">FAQ<br>Pour Donateurs(trices)</div>
  </header>
  <div class="faq-head"><span>QUESTIONS</span><span>RÉPONSES</span></div>
  <div class="faq">
    <div class="faq-row"><span class="q">Quels sont les types de polices admissibles?</span><span class="a">Les polices temporaires et les polices permanentes (vie entière et universelles)</span></div>
    <div class="faq-row"><span class="q">Qui prend en charge la souscription médicale?</span><span class="a">La Fondation</span></div>
    <div class="faq-row"><span class="q">Qui prend en charge la souscription actuarielle?</span><span class="a">La Fondation</span></div>
    <div class="faq-row"><span class="q">Quels montants d’assurance acceptez-vous?</span><span class="a">Entre 50 000 $ et 10 M $</span></div>
    <div class="faq-row"><span class="q">Quels sont vos critères de sélection?</span><span class="a">À la base, l’espérance de vie (EV) de l’assuré ne doit pas dépasser cinq ans. Toutefois, dans certains cas, un assuré peut être admissible même s’il a une espérance de vie supérieure à cinq ans. Voici notre règle empirique : l’assuré a au moins 70 ans et il a des problèmes de santé ou il a au moins 80 ans et il est en bonne santé.</span></div>
    <div class="faq-row"><span class="q">Qui assume le paiement des primes après le don de la police?</span><span class="a">La Fondation</span></div>
    <div class="faq-row"><span class="q">Qui est le bénéficiaire de la police après qu’elle a été offerte en don?</span><span class="a">La Fondation</span></div>
    <div class="faq-row"><span class="q">Qui est propriétaire de la police après qu’elle a été offerte en don?</span><span class="a">La Fondation</span></div>
    <div class="faq-row"><span class="q">Qui prend en charge les procédures relatives au contrôle préalable et aux souscriptions?</span><span class="a">La Fondation a établi un partenariat avec les Services caritatifs ALDERON, qui s’occupent de ces questions</span></div>
    <div class="faq-row"><span class="q">Comment le processus se déroule-t-il?</span><span class="a">Vous communiquez avec nous par téléphone ou par courriel, en nous fournissant les renseignements suivants :
      <ul><li>La valeur nominale de la police</li><li>Le montant de la prime annuelle (montant actuel et montant au moment du renouvellement)</li><li>Le type de police dont il s’agit</li><li class="minor">S’il s’agit d’une assurance temporaire, est-elle convertible sans souscription médicale?</li><li>La date d’expiration de la police</li><li>Les problèmes de santé de l’assuré</li><li>L’âge de l’assuré</li></ul></span></div>
    <div class="faq-row"><span class="q">Depuis combien de temps la police doit-elle être en vigueur?</span><span class="a">La police doit être en vigueur depuis plus de deux ans.</span></div>
    <div class="faq-row"><span class="q">Sur combien de temps le processus s’échelonne-t-il?</span><span class="a">Triage: moins d’une semaine<br>Souscription médicale : 1 à 2 semaines<br>Souscription actuarielle : 1 semaine<br>Formalités relatives au don : 1 jour<br><b>Durée totale : 3 à 4 semaines</b></span></div>
    <div class="faq-row"><span class="q">Quel est généralement le montant du reçu aux fins d’impôt qui est remis au donateur?</span><span class="a">Ce montant varie selon les prévisions de l’espérance de vie de l’assuré, qui reposent sur son âge et son état de santé.</span></div>
    <div class="faq-row"><span class="q">Que se passe-t-il si l’un de mes proches parents souhaite devenir bénéficiaire de la police?</span><span class="a">Avant d’approuver le don d’une police, nous devons nous assurer qu’aucun proche parent ne souhaite se porter acquéreur de celle-ci.</span></div>
    <div class="faq-row"><span class="q">Un tel don est-il légal?</span><span class="a">Oui, tout le processus est légal, éthique et approuvé par le gouvernement.</span></div>
    <div class="faq-row"><span class="q">Mais qu’est-ce que j’y gagne?</span><span class="a">Vous aviez prévu annuler votre police afin de ne plus avoir à assumer le paiement des primes. La Fondation assume le paiement de celles-ci (vous faites donc une économie d’argent), et vous obtenez en retour un reçu aux fins de l’impôt qui vous permet d’en tirer un avantage pécuniaire.</span></div>
  </div>
  <footer class="footer">Contactez-nous: 1 (800) 555-0142 | donation@varnekholtcanada.org</footer>
</section>

<!-- English charity services -->
<section class="page charity col-left row-3">
  <header class="masthead">
    <div class="masthead-pattern" role="img" aria-label="Soft dotted pattern in pale blue"></div>
    <div class="brand"><div><span class="brand-name">Varnek-Holt</span><span class="brand-sub">Syndrome Foundation Canada</span></div><span class="brand-mark"></span></div>
    <div class="doc-title three">Charity<br>Services<br>For Donors</div>
  </header>
  <div class="band">Unlock the hidden value in your life insurance</div>
  <div class="advantages">
    <h3>ADVANTAGES OF DONATING A LIFE INSURANCE POLICY</h3>
    <ol>
      <li>You obtain a tax receipt (good for 5 years) for 10%-50% of the face value of the policy (even for term policies that have no “cash surrender value”)</li>
      <li>You convert a “worthless or low cash value policy” into cash in your pocket when you file your income taxes</li>
      <li>Eliminate the burden of annual premium expenses</li>
      <li>A Foundation becomes the owner and beneficiary, and it funds the premiums and collects the benefit upon maturity</li>
    </ol>
    <div class="split">
      <p>You can maintain or substantially improve your financial position by unlocking the hidden value of your unwanted or unaffordable life insurance via a charitable donation. Every year, seniors over the age of 70 lapse or surrender almost $7 billion of insurance that they might otherwise donate to a charity. You can pay down debt, make major purchases or replenish retirement savings by accessing the value you deserve after paying premiums for decades.</p>
      <div class="suitable">
        <h4>SUITABLE POLICIES</h4>
        <ul><li>Term, Whole life, Universal or term to 100 policies</li><li>Insured lives over 70 years old</li><li>In-force greater than 2 years</li><li>Minimum death benefit of $50,000</li></ul>
      </div>
    </div>
  </div>
  <div class="band" style="margin-top:5px">Maintain financial independence</div>
  <ul class="benefits">
    <li>Fund retirement living or long-term care expenses through lowered income taxes as a result of the tax receipt</li>
    <li>Reallocate proceeds from the tax receipt and savings to income producing financial assets or annuities</li>
    <li>Reduce or pay off outstanding debts</li>
  </ul>
  <div class="band">Donation process</div>
  <div class="flow">
    <div class="flow-step">Complete Application Form &amp; Provide Policy Documents and Illustration</div>
    <div class="flow-arrow"><svg viewBox="0 0 3 4"><path d="M0 0L3 2L0 4Z" fill="#2c79a7"/></svg></div>
    <div class="flow-step">Provide Medical Information</div>
    <div class="flow-arrow"><svg viewBox="0 0 3 4"><path d="M0 0L3 2L0 4Z" fill="#2c79a7"/></svg></div>
    <div class="flow-step">Determine Amount of Tax Receipt</div>
    <div class="flow-arrow"><svg viewBox="0 0 3 4"><path d="M0 0L3 2L0 4Z" fill="#2c79a7"/></svg></div>
    <div class="flow-step">Sign Ownership Transfer Documents</div>
    <div class="flow-arrow"><svg viewBox="0 0 3 4"><path d="M0 0L3 2L0 4Z" fill="#2c79a7"/></svg></div>
    <div class="flow-step">Convert the Tax Receipt into $$$ in your Pocket</div>
  </div>
  <footer class="footer">Call Us: 1 (800) 555-0142 | donation@varnekholtcanada.org</footer>
  <div class="disclosures">
    <strong>Disclosures</strong>
    Proceeds are treated as a disposition for tax purposes and are taxed on excess amount over adjusted cost basis, which includes all premiums paid on the policy less the net cost of pure insurance.<br>
    Policyholders should seek their own independent professional tax, legal and financial advice.<br>
    A change of ownership of a policy may in the future limit the insured’s ability to purchase additional insurance as a result of limits on how much coverage insurers will issue.<br>
    Donors of life insurance policies will be required to provide consent to allow access to medical records for purposes of evaluating the life insurance policy. This information will be maintained on a confidential basis.
  </div>
</section>

<!-- French charity services -->
<section class="page charity col-right row-3" lang="fr">
  <header class="masthead">
    <div class="masthead-pattern" role="img" aria-label="Motif de points bleu pâle"></div>
    <div class="brand"><div><span class="brand-name">Varnek-Holt</span><span class="brand-sub">Syndrome Foundation Canada</span></div><span class="brand-mark"></span></div>
    <div class="doc-title three">Services<br>Caritatifs<br>Pour Donateurs(trices)</div>
  </header>
  <div class="band">Accédez à la juste valeur de votre police d’assurance-vie</div>
  <div class="advantages">
    <h3>AVANTAGES DU DON D’UNE POLICE D’ASSURANCE-VIE</h3>
    <ol>
      <li>Obtenez un reçu fiscal (bon pour 5 ans) de 10 à 50% de la prestation nette de décès (même pour des polices temporaires n’ayant pas de « valeur de rachat »)</li>
      <li>Convertissez une « police qui n’a peu ou aucune valeur de rachat » en argent dans vos poches quand vous soumettez vos impôts</li>
      <li>Éliminez le fardeau de primes annuelles</li>
      <li>La fondation devient le propriétaire et le bénéficiaire de la police d’assurance-vie ; elle en finance les primes et récupérera la prestation à l’atteinte de sa maturité</li>
    </ol>
    <div class="split">
      <p>Le don d’un contrat d’assurance-vie peut vous aider à maintenir votre autonomie financière. Chaque année, les aînés renoncent à plus de 7 milliards de dollars en polices d’assurance qui pourraient autrement être récupérées à leur juste valeur. En faisant don de votre police d’assurance-vie, vous pouvez accéder à du capital supplémentaire pour rembourser des dettes, faire des achats importants ou renflouer votre épargne retraite.</p>
      <div class="suitable">
        <h4>POLICES ÉLIGIBLES</h4>
        <ul><li>Polices d’assurance temporaires, vie entières, universelles ou temporaires 100 ans</li><li>Polices d’assurance-vie pour les plus de 70 ans</li><li>En vigueur pour plus de deux ans</li><li>Prestation minimale au décès de 50 000 $</li></ul>
      </div>
    </div>
  </div>
  <div class="band" style="margin-top:5px">Maintenez votre autonomie financière</div>
  <ul class="benefits">
    <li>Financement de dépenses liées à la retraite ou à des soins de longue durée grâce à la réduction de l’impôt à la suite du reçu fiscal</li>
    <li>Réallocation des bénéfices vers des rentes ou des actifs produisant des revenus</li>
    <li>Réduction ou paiement de dettes en suspens</li>
  </ul>
  <div class="band">Processus de don</div>
  <div class="flow">
    <div class="flow-step">Compléter le formulaire et fournir les documents et illustrations de polices</div>
    <div class="flow-arrow"><svg viewBox="0 0 3 4"><path d="M0 0L3 2L0 4Z" fill="#2c79a7"/></svg></div>
    <div class="flow-step">Fournir l’information médicale</div>
    <div class="flow-arrow"><svg viewBox="0 0 3 4"><path d="M0 0L3 2L0 4Z" fill="#2c79a7"/></svg></div>
    <div class="flow-step">Déterminer le montant du reçu fiscal</div>
    <div class="flow-arrow"><svg viewBox="0 0 3 4"><path d="M0 0L3 2L0 4Z" fill="#2c79a7"/></svg></div>
    <div class="flow-step">Signer les documents de transfert de propriété</div>
    <div class="flow-arrow"><svg viewBox="0 0 3 4"><path d="M0 0L3 2L0 4Z" fill="#2c79a7"/></svg></div>
    <div class="flow-step">Convertir le reçu fiscal en argent dans vos poches</div>
  </div>
  <footer class="footer">Contactez-nous: 1 (800) 555-0142 | donation@varnekholtcanada.org</footer>
  <div class="disclosures">
    <strong>Divulgation</strong>
    Les titulaires de polices doivent demander leur propre avis professionnel, fiscal, juridique et financier.<br>
    Le produit est traité comme une disposition pour fins d’impôt et est imposé sur l’excédent par rapport au coût rajusté, ce qui comprend toutes les primes payées sur le contrat, moins le coût net de l’assurance pure.<br>
    Le changement de propriété d’une police peut limiter la capacité de l’assuré à souscrire à une éventuelle assurance en raison des limites de la couverture que les assureurs délivreront.<br>
    Les donateurs de polices d’assurance-vie devront donner leur consentement pour permettre l’accès à leurs dossiers médicaux pour fins d’évaluation de la police d’assurance-vie. Ces renseignements demeureront confidentiels.
  </div>
</section>

</body>
</html>
```